Visitenkarten-Design für Rohrreinigungsfirma
Zielgruppe
Wir sind eine Kanal.-Rohrreinigungsfirma und suchen ein hochwertiges Design, unsere Zielgruppe sind Firmenkunden,Hausverwaltungen, Architekten sowie Behörden.
Aufgabenstellung
Das Design sollte Edel aussehen. Es sollten unsere Dienstleistungen mit auf der Visitenkarte stehen (gerne auch Rückseite): grabenlose Kanalsanierung, TV-Kamerainspektion,Dichtheitsprüfung DIN EN 1610, Fräsarbeiten mit Roboter, Fräsarbeiten mit Wasserhöchstdruck 2.500 Bar,Verstopfungsbeseitigung. (Vorderseite sollte enthalten:

```html
<!DOCTYPE html>
<html lang="de">
<head>
<meta charset="utf-8">
<title>Visitenkarte KVR Kanal- &amp; Rohrreinigung</title>
<link rel="stylesheet" href="https://fonts.googleapis.com/css2?family=Raleway:wght@500;600;700;800&display=swap">
<style>
  :root {
    --page: #ffffff;
    --blue: #375e83;
    --navy: #2b3447;
    --red: #b3161f;
    --ink: #2e3646;
    --white: #ffffff;
  }
  * { box-sizing: border-box; margin: 0; padding: 0; }
  html, body {
    width: 898px; height: 1200px; overflow: hidden;
    background: var(--page);
    font-family: "Raleway", Arial, sans-serif;
    font-variant-numeric: lining-nums;
    font-feature-settings: "lnum" 1;
    color: var(--ink);
  }
  .canvas { position: relative; width: 898px; height: 1200px; }
  .side-title {
    position: absolute; left: 0; width: 898px; text-align: center;
    font-size: 29px; font-weight: 700; color: var(--ink);
  }
  .side-title.front { top: 72px; }
  .side-title.back { top: 642px; }

  .card {
    position: absolute; width: 545px; height: 354px; overflow: hidden;
    background: var(--white);
    box-shadow: 0 2px 8px rgba(0,0,0,0.18);
  }
  .card.front { left: 168px; top: 161px; }
  .card.back { left: 170px; top: 727px; width: 546px; }
  .card-shapes { position: absolute; inset: 0; }

  .abs { position: absolute; white-space: nowrap; }
  .light { color: var(--white); }

  .person-name { left: 18px; top: 98px; font-size: 20px; font-weight: 700; letter-spacing: 0.2px; }
  .person-role { left: 18px; top: 128px; font-size: 15px; font-weight: 600; }
  .person-phone { left: 18px; top: 160px; font-size: 15.5px; font-weight: 600; }
  .address { left: 18px; top: 206px; font-size: 15.5px; font-weight: 600; line-height: 25px; }
  .band-link { font-size: 15.5px; font-weight: 600; }
  .front .band-link { left: 24px; top: 299px; }
  .back .band-link { left: 45px; top: 298px; }

  .brand { left: 242px; top: 22px; display: flex; align-items: center; gap: 10px; }
  .brand-mark { width: 22px; height: 22px; background: var(--blue); }
  .brand-name { font-size: 27px; font-weight: 800; color: var(--blue); letter-spacing: 0.5px; }
  .brand-sub { left: 256px; top: 66px; font-size: 17px; font-weight: 800; color: var(--navy); }
  .brand-hotline { left: 304px; top: 91px; font-size: 12px; font-weight: 700; color: var(--red); letter-spacing: 0.3px; }

  .benefits { position: absolute; left: 283px; top: 127px; list-style: none; }
  .benefits li {
    display: flex; align-items: center; gap: 6px;
    height: 24.5px; font-size: 14px; font-weight: 600; color: var(--ink);
  }
  .tick { width: 14px; height: 14px; flex: none; }

  .hotline {
    position: absolute; left: 328px; top: 246px; width: 189px; height: 81px;
    background: var(--red); border-radius: 4px; color: var(--white);
    display: flex; flex-direction: column; justify-content: center; align-items: center;
    font-size: 17px; font-weight: 800; line-height: 23px;
  }

  .services { position: absolute; left: 34px; top: 52px; list-style: none; color: var(--white); }
  .services li {
    position: relative; padding-left: 17px;
    font-size: 15.5px; font-weight: 600; line-height: 22px; margin-bottom: 9.5px;
  }
  .services li::before {
    content: ""; position: absolute; left: 1px; top: 9px;
    width: 5px; height: 5px; border-radius: 50%; background: var(--white);
  }
  .call-text {
    position: absolute; left: 330px; width: 210px; text-align: center;
    font-size: 19.5px; font-weight: 700; line-height: 27px; color: var(--ink);
  }
  .call-text.question { top: 29px; }
  .call-text.action { top: 113px; }
</style>
</head>
<body>
<main class="canvas">
  <h2 class="side-title front">Vorderseite</h2>

  <section class="card front" aria-label="Visitenkarte Vorderseite">
    <svg class="card-shapes" width="545" height="354" viewBox="0 0 545 354" aria-hidden="true">
      <polygon points="0,0 178,0 312,354 0,354" fill="var(--blue)"/>
      <rect x="0" y="282" width="545" height="56" fill="var(--navy)"/>
    </svg>

    <p class="abs light person-name">JONAS FELDNER</p>
    <p class="abs light person-role">Geschäftsführer</p>
    <p class="abs light person-phone">Tel. 06021 - 482 07 16</p>
    <p class="abs light address">Talweg 14<br>63579 Musterstadt/Oberdorf</p>
    <p class="abs light band-link">info@rohrreinigung-kvr.de</p>

    <div class="abs brand">
      <span class="brand-mark"></span>
      <span class="brand-name">KVR</span>
    </div>
    <p class="abs brand-sub">KANAL- &amp; ROHRREINIGUNG</p>
    <p class="abs brand-hotline">24 STUNDEN NOTDIENST</p>

    <ul class="benefits">
      <li><svg class="tick" viewBox="0 0 14 14" aria-hidden="true"><path d="M2 7.5 L5.5 11.5 L12.5 2" fill="none" stroke="var(--red)" stroke-width="2.4" stroke-linecap="round" stroke-linejoin="round"/></svg>transparente Preise</li>
      <li><svg class="tick" viewBox="0 0 14 14" aria-hidden="true"><path d="M2 7.5 L5.5 11.5 L12.5 2" fill="none" stroke="var(--red)" stroke-width="2.4" stroke-linecap="round" stroke-linejoin="round"/></svg>moderne Ausrüstung</li>
      <li><svg class="tick" viewBox="0 0 14 14" aria-hidden="true"><path d="M2 7.5 L5.5 11.5 L12.5 2" fill="none" stroke="var(--red)" stroke-width="2.4" stroke-linecap="round" stroke-linejoin="round"/></svg>regionales Unternehmen</li>
      <li><svg class="tick" viewBox="0 0 14 14" aria-hidden="true"><path d="M2 7.5 L5.5 11.5 L12.5 2" fill="none" stroke="var(--red)" stroke-width="2.4" stroke-linecap="round" stroke-linejoin="round"/></svg>schnell &amp; zuverlässiger Service</li>
    </ul>

    <div class="hotline">
      <span>24H NOTDIENST</span>
      <span>Tag &amp; Nacht</span>
      <span>0151 - 400 700 20</span>
    </div>
  </section>

  <h2 class="side-title back">Rückseite</h2>

  <section class="card back" aria-label="Visitenkarte Rückseite">
    <svg class="card-shapes" width="546" height="354" viewBox="0 0 546 354" aria-hidden="true">
      <polygon points="0,0 279,0 417,354 0,354" fill="var(--blue)"/>
      <rect x="0" y="281" width="546" height="56" fill="var(--navy)"/>
    </svg>

    <ul class="services">
      <li>grabenlose Kanalsanierung</li>
      <li>TV-Kamerainspektion</li>
      <li>Dichtheitsprüfung DIN EN 1610</li>
      <li>Fräsarbeiten mit Roboter</li>
      <li>Fräsarbeiten mit<br>Wasserhöchstdruck 2.500 Bar</li>
      <li>Verstopfungsbeseitigung</li>
    </ul>
    <p class="abs light band-link">www.rohrreinigung-kvr.de</p>

    <p class="call-text question">Abfluss oder<br>Rohr verstopft?</p>
    <p class="call-text action">Jetzt anrufen,<br>wir kommen<br>sofort!</p>

    <div class="hotline">
      <span>24H NOTDIENST</span>
      <span>Tag &amp; Nacht</span>
      <span>0151 - 400 700 20</span>
    </div>
  </section>
</main>
</body>
</html>
```